Business Card Design Project

Im an electrician and my company name is Kestrel Electrical
My main work is installing Lighting and Power Points, Home Theater Systems, TVS, Phones and Data
Im looking a business card, something nice, clean, modern and not to cluttered
Im open to sugestions
I dont mind if the "Services" is on the back on the business card
colours black, grey, white or the blue colour of my logo are prefered but not compulsory
any questions just message me
and please make it so if i need to edit the writing can do it easy. maybe by making it a seperate layer ?
My Details are.
Name - Peter Halloran
Job Title - Licenced Electrician
Mobile - 027 583 2174
Email - peter@kestrelelectrical.co.nz
Web - www.kestrelelectrical.co.nz
Services
Residential / Commercial
Lighting & Power
Heating & Ventilation
Automation
Phone & Data
Home Cinema
Sound Systems
TV, Antenna & Satellite
Digital Upgrades

```html
<!DOCTYPE html>
<html lang="en">
<head>
<meta charset="utf-8">
<title>Kestrel Electrical – Business Card</title>
<link href="https://fonts.googleapis.com/css2?family=Archivo:wght@700&family=Source+Sans+3:wght@400;600;700&display=swap" rel="stylesheet">
<style>
  :root {
    --cyan: #00b3cc;
    --grey: #58595b;
    --black: #0a0b0d;
    --ink: #111111;
    --white: #ffffff;
    --shadow: #1d1d1f;
  }
  * { margin: 0; padding: 0; box-sizing: border-box; }
  html, body { width: 1200px; height: 1000px; overflow: hidden; }
  body {
    position: relative;
    background: var(--white);
    font-family: "Source Sans 3", "Myriad Pro", sans-serif;
    border-top: 2px solid var(--cyan);
    border-bottom: 2px solid var(--cyan);
  }

  /* Front of card */
  .card-front {
    position: absolute; left: 197px; top: 182px;
    width: 360px; height: 607px;
    background: var(--cyan);
    overflow: hidden;
  }
  .card-front .bubble-art { position: absolute; left: 0; top: 0; }
  .company-name {
    position: absolute; left: 40px; top: 118px;
    color: var(--cyan);
    font-weight: 700;
    font-size: 38px;
    line-height: 1.02;
    letter-spacing: 0.5px;
    text-transform: uppercase;
  }
  .holder {
    position: absolute; left: 52px; top: 378px;
    display: inline-block;
    text-align: right;
  }
  .holder-name {
    font-family: "Archivo", "Helvetica Neue", sans-serif;
    font-weight: 700;
    font-size: 38px;
    letter-spacing: -1px;
    color: var(--ink);
    line-height: 1;
  }
  .holder-title {
    font-size: 18px;
    color: var(--ink);
    line-height: 1.2;
    margin-top: 2px;
  }
  .contact {
    position: absolute; left: 47px; top: 498px;
    font-size: 15.5px;
    color: var(--ink);
    line-height: 23px;
  }
  .web-band {
    position: absolute; left: 0; bottom: 0;
    width: 100%; height: 50px;
    background: var(--black);
    color: var(--cyan);
    font-size: 20px;
    display: flex; align-items: center; justify-content: center;
  }

  /* Back of card */
  .card-back {
    position: absolute; left: 628px; top: 182px;
    width: 361px; height: 609px;
    background: var(--black);
  }
  .card-back .top-band {
    height: 31px; background: var(--cyan);
    border-bottom: 4px solid var(--white);
    box-sizing: content-box;
  }
  .services { position: absolute; left: 25px; top: 335px; width: 311px; }
  .services-title {
    color: var(--cyan);
    font-size: 32px;
    font-weight: 400;
    line-height: 1;
    padding-bottom: 4px;
    border-bottom: 1px solid var(--cyan);
  }
  .services-list {
    list-style: none;
    margin-top: 17px;
    color: var(--white);
    font-size: 15.5px;
    line-height: 20.8px;
  }
</style>
</head>
<body>

  <section class="card-front">
    <svg class="bubble-art" width="360" height="607" viewBox="0 0 360 607" aria-hidden="true">
      <polygon points="0,0 360,0 360,100 0,165" fill="var(--grey)"/>
      <path d="M24,92 Q2,104 6,140 L42,272 Q52,306 92,308 L152,293 L122,372 L219,273 L360,229 L360,98 L346,32 Q336,6 306,10 Z"
            fill="var(--shadow)" transform="translate(4,5)"/>
      <path d="M24,92 Q2,104 6,140 L42,272 Q52,306 92,308 L152,293 L122,372 L219,273 L360,229 L360,98 L346,32 Q336,6 306,10 Z"
            fill="var(--white)" stroke="var(--grey)" stroke-width="1.5"/>
    </svg>

    <div class="company-name">Kestrel<br>Electrical</div>

    <div class="holder">
      <div class="holder-name">Peter Halloran</div>
      <div class="holder-title">Licenced Electrician</div>
    </div>

    <div class="contact">
      <div class="contact-mobile">Mobile - 027 583 2174</div>
      <div class="contact-email">Email - peter@kestrelelectrical.co.nz</div>
    </div>

    <div class="web-band">Web - www.kestrelelectrical.co.nz</div>
  </section>

  <section class="card-back">
    <div class="top-band"></div>
    <div class="services">
      <h2 class="services-title">Services</h2>
      <ul class="services-list">
        <li>Residential / Commercial</li>
        <li>Lighting &amp; Power</li>
        <li>Heating &amp; Ventilation</li>
        <li>Automation</li>
        <li>Phone &amp; Data</li>
        <li>Home Cinema</li>
        <li>Sound Systems</li>
        <li>TV, Antenna &amp; Satellite</li>
        <li>Digital Upgrades</li>
      </ul>
    </div>
  </section>

</body>
</html>
```